Save the date for wedding

A save the date for our wedding. We're looking for a simple and sleek invite. I would prefer not alot of calligraphy. Minimalism is good. The basic info to include is as follows:
Names: Mona and Felix
Date: June 9th
Where: Ottawa, Ontario
In small print please include that there will be a reception in Edmonton AB September 1st for those who cannot make it to Ottawa.
Please see the attached file for a style idea. Doesn’t have to be exactly like that, but something like that.

```html
<!DOCTYPE html>
<html lang="en">
<head>
<meta charset="utf-8">
<title>Save the Date – Mona and Felix</title>
<link rel="stylesheet" href="https://fonts.googleapis.com/css2?family=Josefin+Sans:wght@700&family=Federo&family=Yellowtail&family=Yesteryear&family=Oswald:wght@600&family=Uncial+Antiqua&family=Cherry+Swash:wght@700&display=swap">
<style>
  :root {
    --page-bg: #2b2b2b;
    --card: #b7705c;
    --parchment: #ece4d3;
    --parchment-shade: #ddd1ba;
    --wine: #7d1a1c;
    --wine-dark: #6a1416;
    --amber: #e8972c;
    --rust: #c1672a;
    --charcoal: #454545;
    --gold-text: #f7c872;
    --pill: #fdd28c;
    --splash: #f5bd6c;
  }
  html, body {
    margin: 0;
    width: 1200px;
    height: 1200px;
    overflow: hidden;
    background: var(--page-bg);
  }
  .save-the-date {
    position: absolute;
    left: 196px;
    top: 29px;
    width: 808px;
    height: 1141px;
    display: block;
  }
  .card-base { fill: var(--card); }
  .parchment { fill: url(#parchmentTone); }
  .rule-amber { stroke: var(--amber); stroke-width: 3; }
  .rule-dark { stroke: var(--charcoal); stroke-width: 3; }
  .rule-wine { stroke: var(--wine); stroke-width: 3; }
  .headline {
    font-family: "Josefin Sans", sans-serif;
    font-weight: 700;
    font-size: 96px;
    letter-spacing: -4px;
    fill: var(--wine);
  }
  .subheadline {
    font-family: "Federo", sans-serif;
    font-size: 80px;
    fill: var(--amber);
  }
  .couple-name {
    font-family: "Yellowtail", cursive;
    font-size: 92px;
    fill: var(--wine);
  }
  .couple-joiner {
    font-family: "Yellowtail", cursive;
    font-size: 74px;
    fill: var(--charcoal);
  }
  .celebration {
    font-family: "Yesteryear", cursive;
    font-size: 82px;
    fill: var(--rust);
  }
  .flourish { fill: url(#flourishTone); }
  .date-ribbon { fill: var(--wine); }
  .date-text {
    font-family: "Oswald", sans-serif;
    font-weight: 600;
    font-size: 66px;
    fill: var(--gold-text);
  }
  .venue-label {
    font-family: "Yesteryear", cursive;
    font-size: 42px;
    fill: var(--wine-dark);
  }
  .venue-pill { fill: var(--pill); }
  .venue-text {
    font-family: "Uncial Antiqua", serif;
    font-size: 38px;
    fill: #1f1a14;
  }
  .reception-band { fill: var(--splash); }
  .reception-note {
    font-family: "Cherry Swash", serif;
    font-weight: 700;
    font-size: 30px;
    fill: var(--wine);
  }
</style>
</head>
<body>
<svg class="save-the-date" viewBox="0 0 878 1240" xmlns="http://www.w3.org/2000/svg" role="img" aria-label="Save the date for the wedding of Mona and Felix, June 9th, Ottawa, Ontario">
  <defs>
    <radialGradient id="parchmentTone" cx="50%" cy="45%" r="65%">
      <stop offset="0%" stop-color="#f1eadb"/>
      <stop offset="70%" stop-color="#e8dfcb"/>
      <stop offset="100%" stop-color="#dccfb6"/>
    </radialGradient>
    <linearGradient id="flourishTone" x1="0" x2="1">
      <stop offset="0%" stop-color="#e6dccb" stop-opacity="0"/>
      <stop offset="50%" stop-color="#c79a86" stop-opacity="0.55"/>
      <stop offset="100%" stop-color="#e6dccb" stop-opacity="0"/>
    </linearGradient>
    <path id="nameArc" d="M 110 545 Q 430 380 780 520"/>
  </defs>

  <rect class="card-base" x="0" y="0" width="878" height="1240"/>
  <rect class="parchment" x="30" y="52" width="820" height="1150" rx="6"/>

  <line class="rule-amber" x1="128" y1="118" x2="758" y2="118"/>
  <text class="headline" x="443" y="220" text-anchor="middle">SAVE THE DATE</text>
  <text class="subheadline" x="443" y="322" text-anchor="middle">FOR THE WEDDING</text>
  <line class="rule-dark" x1="128" y1="347" x2="758" y2="347"/>

  <text text-anchor="middle">
    <textPath href="#nameArc" startOffset="50%">
      <tspan class="couple-name">Mona </tspan><tspan class="couple-joiner">and </tspan><tspan class="couple-name">Felix</tspan>
    </textPath>
  </text>
  <text class="celebration" x="440" y="568" text-anchor="middle">celebration</text>

  <rect class="flourish" x="160" y="590" width="560" height="135" rx="60" role="img" aria-label="Decorative scrolled flourish ornament"/>

  <line class="rule-wine" x1="88" y1="740" x2="792" y2="740"/>
  <path class="date-ribbon" d="M 80 757 L 800 757 L 762 796 L 800 835 L 80 835 L 118 796 Z"/>
  <text class="date-text" x="440" y="823" text-anchor="middle">DATE: JUNE 9TH</text>
  <line class="rule-wine" x1="88" y1="852" x2="792" y2="852"/>

  <text class="venue-label" x="145" y="925">venue</text>
  <rect class="venue-pill" x="263" y="890" width="450" height="50" rx="20"/>
  <text class="venue-text" x="488" y="930" text-anchor="middle">OTTAWA, ONTARIO</text>

  <path class="reception-band" d="M 42 995 Q 200 975 420 985 Q 640 970 805 990 L 800 1130 Q 600 1118 420 1128 Q 220 1138 45 1125 Z"/>
  <text class="reception-note" x="440" y="1052" text-anchor="middle">Reception in Edmonton AB September 1st</text>
  <text class="reception-note" x="440" y="1092" text-anchor="middle">for those who cannot make it to Ottawa.</text>
</svg>
</body>
</html>
```